Baby Care Print Log for Nannies and Parents- Creating a brand/style I can use across different forms

I am creating a notebook for babysitters to use to communicate with parents about the children they care for. I will be creating many different forms (emergency contacts, daily logs, shopping lists, etc.)
I need a look and feel from which to style these forms from. I am starting by designing the daily baby care log. I need a designer to take my Word doc with just text on it, and create a visual approach to make this visually appealing.
I do not want this to be extremely "babyish" with cartoon styling. I want it to be more of a professional looking style. I would like to be able to color each different document a different color palette, yet keep the similar look and feel. My logo is attached for inspiration. I use real photography across my website velmorapath.com.
Updates
I will be re-designing my Wordpress website based on what design I like best and also will need other forms completed once I pick a design. I am hoping to work with someone who I can hire for further development needs as well. Added Saturday, February 11, 2017
Target Market(s)
Professional Parents
Industry/Entity Type
Education
Requirements
Must have
- color, pop, visual appeal
- Please use the color in my logo and any complementary colors that you think work well with it. I definitely like colored patterns, ombre, colored backgrounds, etc. I'd prefer for it not to be completely white with only pops of color here and there.
Nice to have
- My logo somewhere subtly on the form
- Photography elements
Should not have
- cartoon images of babies, etc. I use real photography across my website with the exception of my logo umbrella.

```html
<!DOCTYPE html>
<html lang="en">
<head>
<meta charset="utf-8">
<title>Velmora Notes – Daily Log</title>
<link href="https://fonts.googleapis.com/css2?family=Open+Sans:wght@400;600;700&display=swap" rel="stylesheet">
<style>
  :root {
    --pink-deep: #ee5ea6;
    --pink-mid: #f48cc1;
    --pink-soft: #fbd7ea;
    --pink-pale: #fff3f8;
    --ink: #e0358f;
    --line: rgba(247, 216, 120, 0.55);
    --box-fill-top: rgba(255, 255, 255, 0.55);
    --box-fill-bottom: rgba(255, 255, 255, 0.85);
    --white: #ffffff;
  }
  * { box-sizing: border-box; margin: 0; padding: 0; }
  html, body { width: 901px; height: 1200px; overflow: hidden; background: var(--white); }
  .sheet {
    position: relative;
    width: 901px;
    height: 1200px;
    font-family: "Open Sans", sans-serif;
    color: var(--ink);
    background:
      repeating-linear-gradient(to bottom, transparent 0 28px, var(--line) 28px 30px) 0 240px / 100% 960px no-repeat,
      linear-gradient(to bottom, var(--pink-deep) 0%, var(--pink-mid) 22%, var(--pink-soft) 55%, var(--pink-pale) 100%);
  }
  .title {
    position: absolute;
    left: 0; right: 0; top: 16px;
    text-align: center;
    color: var(--white);
    font-weight: 400;
    font-size: 84px;
    letter-spacing: 1px;
    line-height: 1.2;
  }
  .box {
    position: absolute;
    border: 2px solid var(--pink-deep);
    border-radius: 12px;
    background: linear-gradient(to bottom, var(--box-fill-top), var(--box-fill-bottom));
  }
  .box-heading {
    position: absolute;
    left: 0; right: 0; top: 10px;
    text-align: center;
    font-weight: 700;
    font-size: 21px;
  }
  .column-label {
    position: absolute;
    top: 64px;
    font-weight: 700;
    font-size: 13px;
    text-decoration: underline;
  }
  .name-bar {
    left: 56px; top: 138px; width: 791px; height: 60px;
    background: var(--white);
  }
  .field-label {
    position: absolute;
    top: 16px;
    font-weight: 700;
    font-size: 21px;
  }
  .field-divider {
    position: absolute;
    left: 512px; top: 6px; bottom: 6px;
    border-left: 2px solid var(--pink-deep);
  }
  .activities { left: 56px; top: 213px; width: 791px; height: 252px; }
  .naps { left: 56px; top: 478px; width: 387px; height: 239px; }
  .diapers { left: 458px; top: 478px; width: 389px; height: 239px; }
  .feeding { left: 56px; top: 731px; width: 791px; height: 254px; }
  .feeding .column-label { top: 46px; }
  .special-notes { left: 56px; top: 997px; width: 514px; height: 178px; }
  .special-notes .box-heading { top: 18px; }
  .mood { left: 584px; top: 1004px; width: 263px; height: 98px; }
  .mood .box-heading { text-align: left; left: 16px; top: 8px; }
  .brand-name {
    position: absolute;
    right: 54px; top: 1134px;
    font-weight: 700;
    font-size: 21px;
    color: var(--ink);
  }
</style>
</head>
<body>
<main class="sheet">
  <h1 class="title">VELMORA NOTES</h1>

  <section class="box name-bar">
    <span class="field-label" style="left:8px">NAME</span>
    <span class="field-divider"></span>
    <span class="field-label" style="left:522px">DATE</span>
  </section>

  <section class="box activities">
    <h2 class="box-heading">TODAY’S ACTIVITES</h2>
  </section>

  <section class="box naps">
    <h2 class="box-heading">NAPS</h2>
    <span class="column-label" style="left:31px">TIME</span>
    <span class="column-label" style="left:232px">LENGTH</span>
  </section>

  <section class="box diapers">
    <h2 class="box-heading">DIAPERS</h2>
    <span class="column-label" style="left:14px">TIME</span>
    <span class="column-label" style="left:177px">WET</span>
    <span class="column-label" style="left:315px">BM</span>
  </section>

  <section class="box feeding">
    <h2 class="box-heading">FEEDING</h2>
    <span class="column-label" style="left:35px">TIME</span>
    <span class="column-label" style="left:234px">MILK</span>
    <span class="column-label" style="left:488px">WATER</span>
    <span class="column-label" style="left:671px">FOOD</span>
  </section>

  <section class="box special-notes">
    <h2 class="box-heading">SPECIAL NOTES/GROCERIES</h2>
  </section>

  <section class="box mood">
    <h2 class="box-heading">MOOD</h2>
  </section>

  <p class="brand-name">VELMORA NOTES</p>
</main>
</body>
</html>
```